Print Ad Design

I need an ad designed to promote an event that we are hosting at a trade show for placement in the show program. The art must be ready to submit to the publication by Friday, November 15th at the latest. The ad is 1/2 page in the show program that will be 4.25"X 5.5" and must be submitted as a high resolution (300dpi) PDF. Ad is full colour. The minimum bleed and trim marks are 0.25". The trade show is the Northern Herd Fair in Canada and we would like to promote a 2 day training we will be hosting at the close of the show. Our company is PastureLink Systems - Ultrasound and Diagnostics and the details that should be included in the ad are:
YOU CAN USE ULTRASOUND TO MANAGE YOUR PREG CHECKS
On Farm Ultrasound Training for Producers
When - Friday, Feb. 7th & Saturday, Feb. 8th
9 AM - 5 PM
Where - close to Herd FAIR
Lunch provided
Registration $175 per day - $300 total
Introduction to ultrasound
Reproductive system anatomy
Pregnancy diagnosis
Live on farm scanning demonstrations and practice with case discussions
Tuition redeemable towards the purchase of ultrasound system.
TO REGISTER OR LEARN MORE
email - info@pasturelinksystems.ca or call 1-800-555-0147
(I have attached our logo and some possible images to use in the ad)
Please note that the primary logo to feature is PastureLink Systems and the secondary logo to use in the ad is Velorek Ultrasound Scanners.
THANK YOU!!!
Target Market(s)
Dairy Farmers (men and women)
Industry/Entity Type
Trade
Look and feel

```html
<!DOCTYPE html>
<html lang="en">
<head>
<meta charset="utf-8">
<title>On Farm Ultrasound Training – PastureLink Systems</title>
<link href="https://fonts.googleapis.com/css2?family=Roboto+Condensed:wght@400;700&display=swap" rel="stylesheet">
<style>
  :root {
    --stage: #404040;
    --guide: #8a8a8a;
    --navy: #1a5483;
    --navy-deep: #16466f;
    --gold: #f8c614;
    --white: #ffffff;
  }
  * { margin: 0; padding: 0; box-sizing: border-box; }
  html, body { width: 1200px; height: 1000px; overflow: hidden; background: var(--stage); }
  body { position: relative; font-family: "Roboto Condensed", sans-serif; }

  .guide-h { position: absolute; top: 77px; height: 1px; background: var(--guide); }
  .guide-v { position: absolute; left: 53px; width: 1px; background: var(--guide); }
  .guide-label { position: absolute; color: #9a9a9a; font-size: 15px; }

  .ad {
    position: absolute; left: 99px; top: 113px; width: 1003px; height: 774px;
    background: var(--navy); overflow: hidden;
    box-shadow: 0 4px 10px rgba(0,0,0,.5);
  }
  .masthead { position: absolute; left: 0; top: 0; width: 692px; height: 102px; background: var(--white); }
  .headline {
    position: absolute; left: 19px; top: 22px; color: var(--navy);
    font-size: 41px; line-height: 36px; text-transform: uppercase; letter-spacing: -0.3px;
  }
  .headline strong { font-weight: 700; }
  .gold-rule { position: absolute; left: 0; top: 96px; }

  .event-marker { position: absolute; left: 11px; top: 130px; width: 47px; height: 149px; background: var(--gold); }
  .event-title {
    position: absolute; left: 72px; top: 130px; color: var(--white);
    font-weight: 700; font-size: 29px; line-height: 30px; text-transform: uppercase;
  }
  .event-details { position: absolute; left: 72px; top: 200px; color: var(--white); font-size: 20px; line-height: 29.5px; text-transform: uppercase; }
  .event-details b { color: var(--gold); font-weight: 700; }
  .event-details sup { font-size: 11px; }

  .agenda-band {
    position: absolute; left: 0; top: 302px; width: 692px; height: 162px;
    background: linear-gradient(90deg, var(--white) 0, var(--white) 66%, rgba(255,255,255,0) 84%);
  }
  .agenda { position: absolute; left: 72px; top: 311px; list-style: none; font-size: 22px; line-height: 29px; color: var(--navy); }
  .agenda .accent { color: var(--gold); }

  .tuition { position: absolute; left: 72px; top: 474px; color: var(--white); font-size: 27px; line-height: 30px; }
  .divider {
    position: absolute; left: 72px; top: 555px; width: 430px; height: 5px;
    background: linear-gradient(90deg, var(--gold) 70%, rgba(248,198,20,0));
  }
  .register { position: absolute; left: 72px; top: 574px; color: var(--white); }
  .register-title { color: var(--gold); font-weight: 700; font-size: 34px; line-height: 34px; }
  .register-sub { font-size: 19px; line-height: 20px; text-transform: uppercase; }
  .contact { margin-top: 10px; font-size: 24px; line-height: 27px; }

  .partner { position: absolute; left: 72px; top: 698px; display: flex; align-items: center; gap: 10px; }
  .partner-mark { width: 40px; height: 40px; background: var(--gold); }
  .partner-name { color: var(--white); font-size: 18px; text-transform: uppercase; line-height: 20px; }

  .photo { position: absolute; left: 691px; width: 312px; }
  .photo-scan { top: 0; height: 212px; background: linear-gradient(160deg, #6b5a48, #2f3f5a 55%, #9a8d7c); }
  .photo-tech { top: 212px; height: 420px; background: linear-gradient(150deg, #d9d4c8, #8fb7ad 40%, #2a2a2a 75%, #e8e6e1); }

  .corner { position: absolute; left: 0; top: 0; }
  .brand { position: absolute; left: 525px; top: 627px; display: flex; align-items: center; gap: 22px; }
  .brand-mark { width: 110px; height: 110px; border-radius: 50%; background: var(--gold); }
  .brand-name { color: var(--navy); font-size: 46px; line-height: 48px; }
  .brand-tag { color: var(--navy); font-size: 23px; letter-spacing: 1.5px; margin-top: 4px; }
</style>
</head>
<body>
  <div class="guide-h" style="left:182px;width:358px"></div>
  <div class="guide-h" style="left:622px;width:360px"></div>
  <div class="guide-label" style="left:556px;top:68px">5.5</div>
  <div class="guide-v" style="top:165px;height:565px"></div>
  <div class="guide-label" style="left:38px;top:436px">4.25</div>

  <article class="ad">
    <header class="masthead">
      <h1 class="headline">You can use <strong>ultrasound</strong><br><strong>to manage your preg checks</strong></h1>
    </header>
    <svg class="gold-rule" width="692" height="14" viewBox="0 0 692 14">
      <polygon points="0,4 692,4 692,13 0,8" fill="var(--gold)"/>
    </svg>

    <div class="event-marker"></div>
    <h2 class="event-title">On farm ultrasound training<br>for producers</h2>
    <div class="event-details">
      <div><b>When</b> Friday, Feb. 7<sup>th</sup> &amp; Saturday, Feb. 8<sup>th</sup> 9 AM - 5 PM</div>
      <div><b>Where</b> Close to Herd FAIR</div>
      <div><b>Lunch provided</b> Registration $175 per day - $300 total</div>
    </div>

    <div class="agenda-band"></div>
    <ul class="agenda">
      <li class="accent">Introduction to ultrasound</li>
      <li>Reproductive system anatomy</li>
      <li class="accent">Pregnancy diagnosis</li>
      <li>Live on farm scanning demonstrations<br>and practice with case discussions</li>
    </ul>

    <p class="tuition">Tuition redeemable towards<br>the purchase of ultrasound system.</p>
    <div class="divider"></div>

    <div class="register">
      <div class="register-title">TO REGISTER</div>
      <div class="register-sub">Or learn more</div>
      <div class="contact">info@pasturelinksystems.ca<br>1.800.555.0147</div>
    </div>

    <div class="partner">
      <div class="partner-mark"></div>
      <div class="partner-name">Velorek<br>Ultrasound Scanners</div>
    </div>

    <div class="photo photo-scan" role="img" aria-label="Two technicians performing an ultrasound scan on a dairy cow in a barn"></div>
    <div class="photo photo-tech" role="img" aria-label="Technician holding a handheld ultrasound scanner while examining a Holstein cow"></div>

    <svg class="corner" width="1003" height="774" viewBox="0 0 1003 774">
      <path d="M428 774 C 450 640 650 560 1003 552 L1003 774 Z" fill="var(--gold)"/>
      <path d="M447 774 C 472 656 668 578 1003 568 L1003 774 Z" fill="var(--white)"/>
    </svg>

    <div class="brand">
      <div class="brand-mark"></div>
      <div>
        <div class="brand-name">PastureLink Systems</div>
        <div class="brand-tag">ultrasound and diagnostics</div>
      </div>
    </div>
  </article>
</body>
</html>
```